Stone Meadow Nutraceuticals Hemp derived full spectrum CBD oil label for 300mg and 1000mg bottles

Need a label for our Hemp derived full spectrum CBD oil tinctures. We will be offering a 300mg and a 1000mg bottle. They will both be in 1 oz brown bottle with a black dropper on cap.

Target Market(s)

Health concious person looking for a nutritional supplement to help with managing anxiety, insomnia, inflammation, pain, arthritis, PTSD, nausea, muscle spasms. This type of person shops at Green Basket and high end spa. This person buys organic produce

Font styles to use
Serif
Sans Serif

Colors

Designer to choose colors to be used in the design.

Requirements
Must have
• Clean lines
• Simplicity
• The words, “full spectrum hemp extract”
• 1000mg
Should not have
• Marijuana leaf

```html
<!DOCTYPE html>
<html lang="en">
<head>
<meta charset="utf-8">
<title>Stone Meadow Nutraceuticals – Full Spectrum Hemp Extract Label</title>
<link href="https://fonts.googleapis.com/css2?family=Fira+Sans:wght@500;600&family=Lato:wght@400;700;900&display=swap" rel="stylesheet">
<style>
  :root{
    --navy:#262066;
    --green:#8dc63f;
    --white:#ffffff;
    --edge:#d3d4da;
    --stage:#e4e4e6;
    --ink:#1d1d24;
  }
  html,body{margin:0;padding:0;width:1200px;height:900px;overflow:hidden;background:var(--stage);}
  .label{position:absolute;left:40px;top:190px;width:1120px;height:522px;font-family:"Lato",sans-serif;color:var(--white);
    box-shadow:0 18px 30px rgba(0,0,0,.18);}
  .label-shapes{position:absolute;inset:0;}
  .panel-left,.panel-right,.panel-center{position:absolute;top:0;bottom:0;}

  .boxed{border:2px solid var(--white);box-sizing:border-box;position:absolute;}
  .product-type{left:26px;top:30px;width:269px;height:36px;font-size:19px;font-weight:700;text-align:center;line-height:32px;letter-spacing:.2px;}
  .suggested-use{left:26px;top:79px;width:269px;height:132px;padding:8px 10px;font-size:18px;line-height:22px;}
  .suggested-use strong{font-weight:900;display:block;}
  .disclaimer{position:absolute;left:37px;width:260px;font-size:18px;line-height:22.5px;margin:0;}
  .disclaimer.fda{top:238px;}
  .disclaimer.warning{top:304px;}

  .storage{left:812px;top:30px;width:282px;height:82px;padding:8px 8px;font-size:18px;line-height:22px;}
  .facts{position:absolute;left:807px;top:129px;width:295px;height:237px;background:var(--white);border:3px solid var(--ink);box-sizing:border-box;
    color:var(--ink);padding:6px 8px;font-size:13px;line-height:16px;}
  .facts h3{margin:0;font-size:23px;line-height:26px;font-weight:900;}
  .facts .rule{border-top:3px solid var(--ink);margin:6px 0 6px;}
  .facts .rule.thin{border-top-width:2px;}
  .facts table{width:100%;border-collapse:collapse;font-size:13px;}
  .facts td,.facts th{padding:0;text-align:left;font-weight:400;}
  .facts th{font-weight:900;}
  .facts .dv{text-align:right;}
  .facts .other{font-weight:900;display:block;margin-top:10px;}
  .distributor{position:absolute;left:817px;top:383px;font-size:17px;line-height:20px;margin:0;}

  .brand{position:absolute;left:372px;width:378px;top:24px;text-align:center;color:var(--navy);font-family:"Fira Sans",sans-serif;font-weight:500;}
  .brand-mark{width:66px;height:66px;border-radius:50%;background:var(--navy);margin:0 auto 12px;}
  .brand-name{font-size:38px;line-height:38px;display:block;}
  .brand-sub{font-size:24px;line-height:26px;letter-spacing:1.2px;display:block;}
  .product-title{position:absolute;left:372px;width:378px;top:235px;text-align:center;font-family:"Fira Sans",sans-serif;font-weight:600;
    font-size:57px;line-height:52px;margin:0;color:var(--white);}
  .format{position:absolute;left:372px;width:378px;top:344px;height:26px;display:flex;align-items:center;justify-content:center;gap:18px;
    color:var(--navy);font-weight:900;font-size:16px;letter-spacing:8px;}
  .format::before,.format::after{content:"";height:2px;width:92px;background:var(--navy);}
  .strength{position:absolute;left:372px;width:378px;top:403px;text-align:center;color:var(--ink);font-weight:900;font-size:16px;margin:0;}
  .net{position:absolute;left:372px;width:378px;top:455px;text-align:center;color:var(--ink);font-size:16px;line-height:20px;margin:0;}
</style>
</head>
<body>
<section class="label">
  <svg class="label-shapes" width="1120" height="522" viewBox="0 0 1120 522" aria-hidden="true">
    <rect width="1120" height="522" fill="var(--navy)"/>
    <path d="M322 0 L796 0 Q742 261 812 522 L308 522 Q376 261 322 0 Z" fill="var(--edge)"/>
    <path d="M335 0 L783 0 Q730 261 803 522 L322 522 Q390 261 335 0 Z" fill="var(--white)"/>
    <path d="M372 152 Q561 292 750 152 L750 344 L372 344 Z" fill="var(--green)"/>
    <path d="M372 188 Q561 262 750 188 L750 344 L372 344 Z" fill="var(--navy)"/>
    <rect x="372" y="344" width="378" height="26" fill="var(--green)"/>
  </svg>

  <div class="boxed product-type">HEMP-DERIVED CBD OIL</div>
  <div class="boxed suggested-use">
    <strong>SUGGESTED USE:</strong>
    Shake Well Before Use.<br>Use twice daily as a dietary supplement. Place drops in mouth and swallow.
  </div>
  <p class="disclaimer fda">These Statement have not been evaluated,</p>
  <p class="disclaimer warning">Not intended for use under the age of 18. Do not take if you are pregnant or lactating. Consult your physician before use if you have a medical condition or are taking any medication.</p>

  <div class="brand">
    <div class="brand-mark"></div>
    <span class="brand-name">Stone Meadow</span>
    <span class="brand-sub">Nutraceuticals</span>
  </div>
  <h1 class="product-title">Full Spectrum<br>Hemp Extract</h1>
  <div class="format">TINCTURE</div>
  <p class="strength">Unflavored 300 mg CBD</p>
  <p class="net">DIETARY SUPPLEMENT<br>1 fl oz (30 mL)</p>

  <div class="boxed storage">In order to preserve freshness, store away from heat, light and humidity</div>
  <div class="facts">
    <h3>Supplement Facts</h3>
    Serving Size: 15 drops (1/2 dropper)<br>Serving Per Bottle : about 80
    <div class="rule"></div>
    <table>
      <tr><th>Amount/Serving</th><th></th><th class="dv">% Daily Value</th></tr>
      <tr><td>Cannabidiol (CBD)</td><td>10 mg</td><td class="dv">*</td></tr>
      <tr><td>Cannabigerol (CBG)</td><td>3.3 mg</td><td class="dv">*</td></tr>
    </table>
    <div class="rule thin"></div>
    *daily value not established
    <span class="other">Other Ingredients</span>Olive Oil
  </div>
  <p class="distributor">Distributed by:<br>Stone Meadow Nutraceuticals, LLC<br>412 Orchard Hollow Rd<br>Millbrook, NC 27006<br>833-SMN-HEMP (766-4367)</p>
</section>
</body>
</html>
```